plumbing & gas fitting business card design

We need a business card design for a plumbing & gas fitting company. The company covers commercial, domestic and maintenance work. We would like a modern design communicating efficiency and sophistication. preferred colours would include (red grey & black) or (green grey & black). Please DO NOT include any water droplets.

Industry/Entity Type

Business

Contact Information for Business Card

Vortig Plumbing & Gas, Commercial Domestic & Maintenance, licence no. 617394K, ABN 47215830962, Phone 0417382956, Email vortigplumbingandgas@corvanet.com

```html
<!DOCTYPE html>
<html lang="en">
<head>
<meta charset="utf-8">
<title>Vortig Plumbing &amp; Gas — Business Card</title>
<link rel="stylesheet" href="https://fonts.googleapis.com/css2?family=Source+Sans+3:wght@400;600;700&display=swap">
<style>
  :root {
    --card-grey: #d5d5d8;
    --card-grey-light: #e2e2e5;
    --panel-fill: #e9bea7;
    --panel-edge: #d99475;
    --accent-orange: #ef6a2d;
    --brand-navy: #1d4a73;
    --ink: #111111;
  }
  * { margin: 0; padding: 0; box-sizing: border-box; }
  html, body {
    width: 1200px;
    height: 741px;
    overflow: hidden;
    background: #ffffff;
  }
  .card {
    position: relative;
    width: 1200px;
    height: 741px;
    overflow: hidden;
    font-family: "Source Sans 3", "Myriad Pro", Arial, sans-serif;
    color: var(--ink);
  }
  .card__backdrop {
    position: absolute;
    inset: 0;
    background: radial-gradient(ellipse at 50% 45%, var(--card-grey-light), var(--card-grey));
  }
  .panel {
    position: absolute;
    top: 159px;
    height: 411px;
    background: var(--panel-fill);
    border: 3px solid var(--panel-edge);
    border-radius: 12px;
    opacity: 0.92;
  }
  .panel--edge {
    left: -20px;
    width: 128px;
  }
  .panel--contact {
    left: 493px;
    width: 697px;
  }
  .brand {
    position: absolute;
    left: 150px;
    width: 290px;
    top: 300px;
    text-align: center;
    color: var(--brand-navy);
    font-weight: 700;
  }
  .brand__mark {
    display: block;
    width: 70px;
    height: 70px;
    margin: 0 auto 30px;
    border-radius: 50%;
    background: var(--accent-orange);
  }
  .brand__name {
    font-size: 46px;
    line-height: 46px;
    letter-spacing: 0.5px;
  }
  .contact {
    position: absolute;
    left: 559px;
    top: 200px;
  }
  .contact__name {
    font-size: 58px;
    font-weight: 400;
    line-height: 62px;
    letter-spacing: -1px;
  }
  .contact__role {
    font-size: 38px;
    line-height: 44px;
    color: var(--accent-orange);
    margin-bottom: 8px;
  }
  .contact__line {
    font-size: 30px;
    line-height: 42px;
    white-space: nowrap;
  }
  .contact__label {
    color: var(--accent-orange);
  }
  .contact__line--email {
    font-size: 26px;
  }
  .contact__email {
    font-weight: 700;
  }
</style>
</head>
<body>
  <main class="card">
    <div class="card__backdrop" role="img" aria-label="Soft grey background with a light floral damask pattern"></div>

    <div class="panel panel--edge"></div>
    <div class="panel panel--contact"></div>

    <div class="brand">
      <span class="brand__mark"></span>
      <p class="brand__name">Vortig<br>Plumbing &amp; Gas</p>
    </div>

    <section class="contact">
      <h1 class="contact__name">FULL NAME</h1>
      <p class="contact__role">DESIGNATION</p>
      <p class="contact__line"><span class="contact__label">OFFICE</span> ADDRESS</p>
      <p class="contact__line">ZIP, COUNTRY</p>
      <p class="contact__line"><span class="contact__label">Tel:</span> 0417382956 <span class="contact__label">ABN</span> : 47215830962</p>
      <p class="contact__line"><span class="contact__label">Licence no.:</span> 617394K</p>
      <p class="contact__line contact__line--email"><span class="contact__label">Email:</span> <span class="contact__email">vortigplumbingandgas@corvanet.com</span></p>
    </section>
  </main>
</body>
</html>
```